Roll-Up Banner für Glückswebsite
Das war eine großartige Zusammenarbeit und unserem sehr knappen Zeitplan extrem entgegenkommend. Das design ist gleichzeitig seriös und trotzdem jung und dynamisch! Perfekt!
Zielgruppe
Die Website, www.freudenpfad.de ermöglicht es jedem Interessierten kostenlos mehr über das eigene Lebensglück, persönliche Stärken, und die eigene Lebenszufriedenheit herauszufinden. Interessierte können online Fragebögen ausfüllen, und erhalten neben einer detaillierten Rückmeldung über die eigenen Möglichkeiten und Stärken, Hinweise dazu, wie Sie an Ihrem eigenen Potenzial arbeiten können. Es handelt sich um ein Kooperationsprojekt der Nordischen Vereinigung für Heitere Seelenkunde der Uni Wendelstein, der HK-Lindau, der Health Academy Marbach und der Uni Falkenried. Zielgruppe für das Banner sind Menschen, die selbst mit Klienten im Kontext der Positiven Psychologie arbeiten oder Menschen, die sich Ihrem eigenen Lebensglück zuwenden wollen.
Aufgabenstellung
Es handelt sich um ein Roll-up Banner in den Maßen 1m Breite und 2 Meter Höhe.
Das Banner sollte so angelegt sein, dass es interessierten Besuchern auf Kongressen vermittelt, was es mit der Seite Freudenpfad.de auf sich hat. Also wissenschaftlich evaluierte kostenfreie online-Fragebögen, die Menschen dabei helfen Ihre eigenen Stärken und Potenziale zu entdecken und dem eigenen Glück näher zu kommen.
Es sollte außerdem das Logo der NVHS darauf zu sehen sein, sowie kleiner die Logos der Forschungskooperationspartner, HK-Lindau, Uni Wendelstein, Uni Falkenried, Health Academy Marbach.
Die Farben sollten zum Logo der NVHS passen.

```html
<!DOCTYPE html>
<html lang="de">
<head>
<meta charset="utf-8">
<title>Freudenpfad.de – Roll-Up</title>
<link rel="stylesheet" href="https://fonts.googleapis.com/css2?family=Fira+Sans+Extra+Condensed:wght@700&family=Source+Sans+3:wght@400;600;700&family=Libre+Baskerville:wght@700&display=swap">
<style>
  :root {
    --cream: #f3ecdc;
    --sky-warm: #efe2c8;
    --haze: #c9c3b6;
    --verge: #8f8a5c;
    --road: #6e6962;
    --jacket: #2d3558;
    --shirt-gold: #e2b768;
    --title-green: #6aa551;
    --navy: #1a2f6b;
    --ink: #1c1c1c;
    --white: #ffffff;
    --grad-lime: #9fc23e;
    --grad-teal: #4a9fa3;
    --partner-grey: #55606e;
  }
  html, body {
    margin: 0;
    padding: 0;
    width: 1200px;
    height: 2400px;
    overflow: hidden;
    background: var(--white);
  }
  .banner {
    position: relative;
    width: 1200px;
    height: 2400px;
    overflow: hidden;
    font-family: "Source Sans 3", "Myriad Pro", sans-serif;
  }
  .hero-photo {
    position: absolute;
    left: 0; top: 0;
    width: 1200px; height: 1654px;
    background:
      radial-gradient(ellipse 210px 330px at 600px 1210px, rgba(226,183,104,0.75), rgba(226,183,104,0) 75%),
      radial-gradient(ellipse 360px 260px at 600px 760px, rgba(176,120,80,0.45), rgba(176,120,80,0) 75%),
      linear-gradient(100deg, rgba(45,53,88,0) 14%, rgba(45,53,88,0.35) 22%, rgba(45,53,88,0) 32%, rgba(45,53,88,0) 70%, rgba(45,53,88,0.35) 79%, rgba(45,53,88,0) 88%),
      linear-gradient(90deg, rgba(220,220,215,0) 4%, rgba(220,220,215,0.45) 12%, rgba(220,220,215,0) 34%, rgba(220,220,215,0) 68%, rgba(220,220,215,0.45) 88%, rgba(220,220,215,0) 100%),
      linear-gradient(180deg, var(--cream) 0%, var(--sky-warm) 30%, #e6d6bb 42%, var(--haze) 52%, #b9ab92 58%, var(--verge) 64%, #857c6c 70%, var(--road) 82%, #635f5a 100%);
  }
  .site-title {
    position: absolute;
    left: 0; right: 0; top: 118px;
    margin: 0;
    text-align: center;
    font-family: "Fira Sans Extra Condensed", "Myriad Pro", sans-serif;
    font-weight: 700;
    font-size: 178px;
    line-height: 1;
    letter-spacing: -2px;
    color: var(--title-green);
  }
  .sidebar {
    position: absolute;
    left: 0; top: 1387px;
    width: 416px; height: 1013px;
    background: var(--white);
  }
  .society-card {
    height: 361px;
    background: var(--white);
    box-shadow: 0 10px 16px -6px rgba(0,0,0,0.28);
    display: flex;
    flex-direction: column;
    justify-content: center;
    padding-left: 72px;
    box-sizing: border-box;
  }
  .society-mark {
    display: flex; align-items: center; gap: 18px;
  }
  .society-mark .dot {
    width: 56px; height: 56px;
    border-radius: 50%;
    background: var(--grad-teal);
  }
  .society-acronym {
    font-family: "Libre Baskerville", serif;
    font-weight: 700;
    font-size: 64px;
    line-height: 1;
    color: var(--navy);
    letter-spacing: 3px;
  }
  .society-name {
    margin: 22px 0 0 54px;
    font-size: 21px;
    line-height: 27px;
    color: var(--navy);
  }
  .society-name strong { font-weight: 600; }
  .partners-heading {
    margin: 32px 0 0 66px;
    font-weight: 700;
    font-size: 24px;
    line-height: 30px;
    color: var(--ink);
  }
  .partner-grid {
    display: grid;
    grid-template-columns: 150px 180px;
    grid-template-rows: 60px 60px;
    column-gap: 48px;
    row-gap: 57px;
    margin: 50px 0 0 58px;
  }
  .partner {
    display: flex; align-items: center; gap: 10px;
    font-size: 17px;
    font-weight: 600;
    color: var(--partner-grey);
    line-height: 1.2;
  }
  .partner .mark {
    flex: 0 0 auto;
    width: 16px; height: 16px;
    border-radius: 50%;
    background: var(--partner-grey);
  }
  .message-panel {
    position: absolute;
    left: 416px; top: 1654px;
    width: 784px; height: 746px;
    background: linear-gradient(225deg, var(--grad-teal) 0%, #5aa296 35%, #86b25e 65%, var(--grad-lime) 100%);
    color: var(--white);
  }
  .message-panel p {
    margin: 0 0 0 39px;
    font-size: 42px;
    line-height: 60px;
    font-weight: 400;
  }
  .message-panel .lead { margin-top: 42px; }
  .message-panel .invite { margin-top: 57px; }
</style>
</head>
<body>
<div class="banner">
  <div class="hero-photo" role="img" aria-label="Foto: fröhliches Kind mit Fliegermütze und Papp-Flügeln reckt jubelnd die Arme in die Höhe, Landstraße und Berge im Abendlicht"></div>
  <h1 class="site-title">Freudenpfad.de</h1>

  <aside class="sidebar">
    <div class="society-card">
      <div class="society-mark"><span class="dot"></span><span class="society-acronym">NVHS</span></div>
      <p class="society-name">Nordische Vereinigung für<br><strong>Heitere Seelenkunde</strong></p>
    </div>
    <div class="partners-heading">Forschungskooperation</div>
    <div class="partner-grid">
      <div class="partner"><span class="mark"></span>Uni Wendelstein</div>
      <div class="partner"><span class="mark"></span>HK-Lindau</div>
      <div class="partner"><span class="mark"></span>Health Academy Marbach</div>
      <div class="partner"><span class="mark"></span>Uni Falkenried</div>
    </div>
  </aside>

  <section class="message-panel">
    <p class="lead">Wissenschaftlich evaluierte kostenfreie<br>online-Fragebögen.</p>
    <p class="invite">Entdecken Sie ihre Stärken und Ihr<br>Potenzial um Ihrem eigenen Glück<br>näher zu kommen.</p>
  </section>
</div>
</body>
</html>
```